Veltrano - Mechanic/Collision Center Business Card

We're looking for a business card design for our mechanic/ collision repair shop.

Can be with colours or monochromatic.

See the attached files.

Many thanks

```html
<!DOCTYPE html>
<html lang="pt">
<head>
<meta charset="utf-8">
<title>Veltrano – Business Card</title>
<link href="https://fonts.googleapis.com/css2?family=Open+Sans:wght@400;600;800&display=swap" rel="stylesheet">
<style>
  :root {
    --brand-blue: #1d9ad6;
    --ink: #1f2326;
    --paper: #f7f7f7;
    --rule-grey: #a9acae;
    --backdrop: #e4e6e8;
  }
  * { box-sizing: border-box; margin: 0; padding: 0; }
  html, body {
    width: 1200px; height: 900px; overflow: hidden;
    background: var(--backdrop);
    font-family: "Open Sans", Arial, sans-serif;
    color: var(--ink);
  }
  .canvas {
    width: 1200px; height: 900px;
    display: flex; flex-direction: column;
    align-items: center; justify-content: center; gap: 40px;
  }
  .card {
    width: 620px; height: 400px;
    position: relative; overflow: hidden;
    box-shadow: 0 6px 18px rgba(0,0,0,.18);
  }
  /* Back side */
  .card-back {
    background: var(--brand-blue);
    display: flex; align-items: center; justify-content: center;
  }
  .card-back .wordmark {
    color: #fff; font-weight: 800; font-size: 78px; letter-spacing: 1px;
  }
  /* Front side */
  .card-front { background: var(--paper); }
  .card-front .wordmark {
    position: absolute; top: 62px; left: 0; right: 0;
    text-align: center; font-weight: 800; font-size: 58px;
    color: var(--ink); letter-spacing: 1px;
  }
  .details {
    position: absolute; top: 182px; left: 0; right: 0;
    display: flex; justify-content: center;
  }
  .person {
    width: 250px; text-align: right; padding-right: 24px; padding-top: 6px;
  }
  .person .name { font-size: 25px; font-weight: 600; line-height: 1.1; white-space: nowrap; }
  .person .role { font-size: 14px; font-weight: 600; margin-top: 2px; }
  .person .address { font-size: 17px; font-weight: 600; line-height: 1.3; margin-top: 16px; white-space: nowrap; }
  .divider { width: 1.5px; background: var(--ink); height: 150px; }
  .contacts {
    list-style: none; padding-left: 22px; width: 290px;
    display: flex; flex-direction: column; gap: 12px; padding-top: 12px;
  }
  .contacts li {
    display: flex; align-items: center; gap: 14px;
    font-size: 15px; font-weight: 600; white-space: nowrap;
  }
  .contacts svg { width: 22px; height: 22px; flex: none; }
  .footer-rule {
    position: absolute; left: 0; right: 0; bottom: 36px;
    height: 5px; background: var(--rule-grey);
  }
  .footer-band {
    position: absolute; left: 0; right: 0; bottom: 0;
    height: 34px; background: var(--brand-blue);
  }
</style>
</head>
<body>
<main class="canvas">
  <section class="card card-back">
    <span class="wordmark">VELTRANO</span>
  </section>

  <section class="card card-front">
    <div class="wordmark">VELTRANO</div>

    <div class="details">
      <div class="person">
        <p class="name">Duarte Vilaneve</p>
        <p class="role">Manager</p>
        <p class="address">Rua das Oficinas 42<br>1900-118 Lisboa</p>
      </div>
      <div class="divider"></div>
      <ul class="contacts">
        <li>
          <svg viewBox="0 0 24 24" fill="none" stroke="currentColor" stroke-width="1.4"><rect x="2" y="5" width="20" height="14"/><path d="M2 5l10 8 10-8M2 19l7-7M22 19l-7-7"/></svg>
          veltrano.oficina@mailbox.pt
        </li>
        <li>
          <svg viewBox="0 0 24 24" fill="none" stroke="currentColor" stroke-width="1.4" stroke-linejoin="round"><path d="M6 3l3 4-2 2c1 3 4 6 7 7l2-2 4 3-2 3C10 20 4 14 3 6z"/></svg>
          +351 215550142
        </li>
        <li>
          <svg viewBox="0 0 24 24" fill="none" stroke="currentColor" stroke-width="1.4"><rect x="7" y="2" width="10" height="20" rx="1.5"/><path d="M7 18h10"/></svg>
          +351 915550187
        </li>
        <li>
          <svg viewBox="0 0 24 24" fill="none" stroke="currentColor" stroke-width="1.6"><circle cx="12" cy="12" r="9.5"/></svg>
          www.social.pt/veltrano
        </li>
      </ul>
    </div>

    <div class="footer-rule"></div>
    <div class="footer-band"></div>
  </section>
</main>
</body>
</html>
```